Relaunch configurator for lighting

We just need a new modern design for our configurator
http://lichtkonfigurator.vemtra.at

Design must be responsive

Number of Pages Required

1 page

```html
<!DOCTYPE html>
<html lang="en">
<head>
<meta charset="utf-8">
<title>Lumora LED Solutions – Configurator</title>
<link href="https://fonts.googleapis.com/css2?family=Roboto:wght@400;500;700;900&family=Open+Sans:wght@400;600&display=swap" rel="stylesheet">
<style>
:root{
  --red:#9b0000;
  --ink:#2b2b2b;
  --dark:#222222;
  --footer:#232323;
  --white:#ffffff;
  --pill:#e6e6e6;
  --muted:#3d3d3d;
  --line:#555555;
}
*{box-sizing:border-box;margin:0;padding:0}
html,body{width:879px;height:1200px;overflow:hidden}
body{position:relative;background:var(--white);font-family:"Open Sans",sans-serif;color:var(--ink)}
.abs{position:absolute}

.hero{left:0;top:0;width:879px;height:444px;
  background:linear-gradient(180deg,#2a2d31 0%,#3e4347 30%,#4a3b2c 52%,#7a4a1e 72%,#3a2414 100%)}
.brand{font-family:"Roboto",sans-serif;font-weight:900;font-size:22px;color:var(--white);display:flex;align-items:center;gap:8px;white-space:nowrap}
.brand .dot{width:13px;height:13px;border-radius:50%;background:var(--white)}
.hero-brand{left:82px;top:38px}
.burger{left:770px;top:40px;width:26px}
.burger span{display:block;height:3px;background:var(--white);margin-bottom:4px;border-radius:2px}
.hero-title{left:0;width:879px;top:128px;text-align:center;font-family:"Roboto",sans-serif;font-weight:700;font-size:38px;color:var(--white)}
.hero-sub{left:0;width:879px;top:184px;text-align:center;font-family:"Roboto",sans-serif;font-size:20px;line-height:30px;color:var(--white)}
.btn-outline{left:361px;top:266px;width:157px;height:46px;border:1.5px solid var(--white);color:var(--white);font-family:"Roboto",sans-serif;font-weight:700;font-size:16px;display:flex;align-items:center;justify-content:center}
.dots{left:383px;top:393px;display:flex;gap:4px}
.dots span{width:26px;height:3px;background:rgba(255,255,255,.45);border-radius:2px}
.dots span.on{background:var(--white)}

.card{width:229px;top:485px}
.card .photo{height:176px;border:4px solid var(--white);box-shadow:0 0 0 1px #ddd}
.badge{position:absolute;top:158px;left:20px;width:190px;height:34px;border-radius:17px;background:var(--white);box-shadow:0 1px 3px rgba(0,0,0,.2);display:flex;align-items:center;justify-content:center}
.badge .strip{width:160px;height:22px;border-radius:3px;background:linear-gradient(90deg,#f0d89a,#f7f2e0,#f0d89a)}
.icon-ring{width:98px;height:98px;border-radius:50%;background:var(--white);display:flex;align-items:center;justify-content:center;top:414px}
.icon-ring .core{width:84px;height:84px;border-radius:50%;background:var(--muted);display:flex;align-items:center;justify-content:center}
.icon-ring .core.red{background:var(--red)}
.card-title{width:260px;text-align:center;top:690px;font-family:"Roboto",sans-serif;font-weight:500;font-size:17px;line-height:24px;color:var(--ink)}
.pill{top:745px;width:128px;height:29px;background:var(--pill);border-radius:3px;font-family:"Roboto",sans-serif;font-weight:500;font-size:14px;color:var(--muted);display:flex;align-items:center;justify-content:center}
.field{top:745px;left:594px;width:178px;height:29px;border:1px solid #bbb;border-radius:3px;font-size:10.5px;color:#666;padding-left:10px;display:flex;align-items:center}
.btn{width:210px;height:35px;font-family:"Roboto",sans-serif;font-weight:700;font-size:12px;color:var(--white);display:flex;align-items:center;justify-content:center;gap:6px}
.btn.primary{top:791px;background:var(--red)}
.btn.secondary{top:835px;background:var(--dark)}

.footer{left:0;top:934px;width:879px;height:266px;background:var(--footer);color:var(--white)}
.footer-brand{left:82px;top:30px}
.about{left:82px;top:98px;width:270px;font-size:11.5px;line-height:19.5px}
.col-head{font-family:"Roboto",sans-serif;font-weight:700;font-size:13.5px;top:40px}
.links{left:408px;top:74px;font-size:11.5px;line-height:22px;list-style:none}
.contact{left:550px;top:74px;font-size:11.5px;list-style:none}
.contact li{display:flex;gap:8px;margin-bottom:17px;line-height:17px}
.contact svg{flex:none;margin-top:2px}
.rule{left:82px;top:195px;width:715px;height:1px;background:var(--line)}
.copy{left:81px;top:228px;font-size:11.5px}
.social{left:653px;top:213px;display:flex;gap:6px;list-style:none}
.social li{width:32px;height:32px;border:1.5px solid var(--white);border-radius:50%}
</style>
</head>
<body>

<header class="hero abs" role="img" aria-label="Night aerial view of a city with glowing orange street lights"></header>
<div class="brand hero-brand abs"><span class="dot"></span>LUMORA LED SOLUTIONS</div>
<div class="burger abs"><span></span><span></span><span></span></div>
<h1 class="hero-title abs">LUMORA LED SOLUTIONS</h1>
<p class="hero-sub abs">Individual and stepless setting of the light color<br>from cold white to warm white</p>
<div class="btn-outline abs">INQUIRE NOW!</div>
<div class="dots abs"><span class="on"></span><span></span><span></span><span></span></div>

<div class="card abs" style="left:82px">
  <div class="photo" role="img" aria-label="Gaming desk with monitor and colourful LED lighting" style="background:linear-gradient(135deg,#1c2a6b,#3a1a5a 50%,#6b1f8a)"></div>
  <div class="badge"><div class="strip" role="img" aria-label="Dual white LED strip"></div></div>
</div>
<div class="icon-ring abs" style="left:148px">
  <div class="core">
    <svg width="50" height="50" viewBox="0 0 50 50" fill="none" stroke="#fff" stroke-width="4" stroke-linecap="round">
      <path d="M8 42 L30 20"/><path d="M28 10 a8 8 0 1 0 12 10"/><path d="M10 10 L22 22"/>
      <circle cx="36" cy="38" r="7" stroke-width="3"/><path d="M36 38 l3 -3" stroke-width="2.5"/>
    </svg>
  </div>
</div>
<div class="card-title abs" style="left:67px">Create a new<br>DUO Configuration</div>
<div class="pill abs" style="left:133px">2700k - 6000k</div>
<div class="btn primary abs" style="left:91px">1-12 LEUCHTEN KONFIGURIEREN</div>
<div class="btn secondary abs" style="left:91px">13-24 LEUCHTEN KONFIGURIEREN</div>

<div class="card abs" style="left:326px">
  <div class="photo" role="img" aria-label="Close-up of an RGB LED matrix panel" style="background:linear-gradient(120deg,#05070f,#1a2a3a 45%,#7a5a8a 75%,#f0c0d0)"></div>
  <div class="badge"><div class="strip" role="img" aria-label="RGB LED strip" style="background:linear-gradient(90deg,#e8e2d0,#f2eee4,#e8e2d0)"></div></div>
</div>
<div class="icon-ring abs" style="left:391px">
  <div class="core red">
    <svg width="60" height="60" viewBox="0 0 60 60" fill="none" stroke="#fff" stroke-width="3" font-family="Roboto,sans-serif" font-weight="700" font-size="11">
      <circle cx="30" cy="22" r="12"/><circle cx="22" cy="37" r="12"/><circle cx="38" cy="37" r="12"/>
      <text x="26" y="26" fill="#fff" stroke="none">R</text><text x="14" y="41" fill="#fff" stroke="none">G</text><text x="39" y="41" fill="#fff" stroke="none">B</text>
    </svg>
  </div>
</div>
<div class="card-title abs" style="left:310px">Create a new<br>RGB Configuration</div>
<div class="pill abs" style="left:376px">2700k - 6000k</div>
<div class="btn primary abs" style="left:335px">1-12 LEUCHTEN KONFIGURIEREN</div>
<div class="btn secondary abs" style="left:335px">13-24 LEUCHTEN KONFIGURIEREN</div>

<div class="card abs" style="left:569px">
  <div class="photo" role="img" aria-label="Dark room desk setup with two monitors and gaming chair" style="background:linear-gradient(135deg,#2a2024,#6a4a5a 40%,#3a5a8a 60%,#161214)"></div>
  <div class="badge"><div class="strip" role="img" aria-label="Dual white LED strip"></div></div>
</div>
<div class="icon-ring abs" style="left:634px">
  <div class="core">
    <svg width="50" height="50" viewBox="0 0 50 50" fill="none" stroke="#fff" stroke-width="4" stroke-linecap="round">
      <path d="M38 22 A15 15 0 1 1 26 11"/><path d="M20 32 L40 12 L44 16 L24 36 L18 38 Z" stroke-width="3"/>
    </svg>
  </div>
</div>
<div class="card-title abs" style="left:553px">Load and Edit the<br>Existing Configuration</div>
<div class="field abs">Enter Configuration Number</div>
<div class="btn primary abs" style="left:578px;font-size:12.5px">LADEN</div>
<div class="btn secondary abs" style="left:578px;font-size:12.5px">
  <svg width="12" height="12" viewBox="0 0 12 12" fill="#fff"><path d="M5 0h2v6h2L6 9 3 6h2z"/><rect x="0" y="10" width="12" height="2"/></svg>
  PDF HERUNTERLADEN</div>

<footer class="footer abs">
  <div class="brand footer-brand abs"><span class="dot"></span>LUMORA LED SOLUTIONS</div>
  <p class="about abs">Nemo enim ipsam voluptatem quia voluptas sit aspernatur aut odit aut fugit, sed quia consequu ntur magni dolores eos qui ratione voluptatem sequi nesciun que porro qu.</p>
  <h3 class="col-head abs" style="left:408px">LEGAL</h3>
  <ul class="links abs"><li>Imprint</li><li>Privacy</li><li>Disclaimer</li></ul>
  <h3 class="col-head abs" style="left:550px">CONTACT US</h3>
  <ul class="contact abs">
    <li><svg width="9" height="12" viewBox="0 0 9 12" fill="#fff"><path d="M4.5 0A4.5 4.5 0 0 0 0 4.5C0 8 4.5 12 4.5 12S9 8 9 4.5A4.5 4.5 0 0 0 4.5 0zm0 6.3a1.8 1.8 0 1 1 0-3.6 1.8 1.8 0 0 1 0 3.6z"/></svg><span>Ullam corporis suscipi<br>&nbsp;D-04712 Lindenfeld</span></li>
    <li><svg width="11" height="11" viewBox="0 0 11 11" fill="#fff"><path d="M2.2 0l2 2.6-1.1 1.5a7 7 0 0 0 3.8 3.8L8.4 6.8 11 8.8 9.6 11C4.5 11 0 6.5 0 1.4z"/></svg><span>1 555 010 0100</span></li>
    <li><svg width="13" height="10" viewBox="0 0 13 10" fill="#fff"><path d="M0 0h13v1.5L6.5 5.5 0 1.5zM0 3l6.5 4L13 3v7H0z"/></svg><span>info@lichtkonfigurator.vemtra.at</span></li>
  </ul>
  <div class="rule abs"></div>
  <p class="copy abs">Copyright ©2020. Lumora LED Solutions. All rights reserved.</p>
  <ul class="social abs" aria-label="Social links">
    <li aria-label="Social link 1"></li><li aria-label="Social link 2"></li><li aria-label="Social link 3"></li><li aria-label="Social link 4"></li>
  </ul>
</footer>

</body>
</html>
```